The Perfect Business Card for PineHarbor

I am looking for a business card which beautifully incorporates my logo, reflects my business and looks special, elegant and clean.

```html
<!DOCTYPE html>
<html lang="en">
<head>
<meta charset="utf-8">
<title>PineHarbor Business Card</title>
<link href="https://fonts.googleapis.com/css2?family=Roboto:wght@400;500&display=swap" rel="stylesheet">
<style>
  :root {
    --backdrop: #cdcdcd;
    --card-front: #ffffff;
    --card-back: #050808;
    --brand-green: #6b8e2f;
    --brand-green-dark: #56762a;
    --text-grey: #555555;
    --pin-grey: #c4c4c4;
    --mark-grey: #5f5f5f;
  }
  * { margin: 0; padding: 0; box-sizing: border-box; }
  html, body {
    width: 990px;
    height: 1200px;
    overflow: hidden;
    background: var(--backdrop);
    font-family: "Roboto", Arial, sans-serif;
  }
  .canvas {
    position: relative;
    width: 990px;
    height: 1200px;
  }
  .card {
    position: absolute;
    left: 177px;
    width: 639px;
    height: 369px;
    border-radius: 30px;
  }
  .card--front { top: 123px; background: var(--card-front); }
  .card--back { top: 617px; background: var(--card-back); }

  .brand {
    position: absolute;
    display: flex;
    align-items: center;
  }
  .brand__circle {
    border-radius: 50%;
    flex: none;
  }
  .brand__name {
    font-weight: 500;
    letter-spacing: 0.5px;
    line-height: 1;
  }
  .card--front .brand { left: 48px; top: 118px; gap: 14px; }
  .card--front .brand__circle {
    width: 58px; height: 58px;
    border: 3px solid var(--brand-green);
  }
  .card--front .brand__name { font-size: 34px; color: var(--brand-green); }

  .card--back .brand { left: 82px; top: 150px; gap: 20px; }
  .card--back .brand__circle {
    width: 90px; height: 90px;
    border: 4px solid var(--mark-grey);
  }
  .card--back .brand__name { font-size: 52px; color: var(--mark-grey); }

  .divider {
    position: absolute;
    left: 354px;
    top: 97px;
    width: 3px;
    height: 173px;
    background: var(--brand-green);
  }
  .contact-list {
    position: absolute;
    left: 388px;
    top: 99px;
    list-style: none;
  }
  .contact-list__item {
    display: flex;
    align-items: center;
    height: 28px;
    margin-bottom: 19.5px;
    font-size: 17px;
    color: var(--text-grey);
  }
  .contact-list__icon {
    width: 28px;
    height: 28px;
    border-radius: 7px;
    background: linear-gradient(180deg, #7fa33a, var(--brand-green-dark));
    margin-right: 16px;
    display: flex;
    align-items: center;
    justify-content: center;
  }
  .address {
    position: absolute;
    left: 0;
    width: 100%;
    top: 312px;
    display: flex;
    justify-content: center;
    align-items: center;
    gap: 7px;
    font-size: 17px;
    color: var(--text-grey);
  }
</style>
</head>
<body>
<main class="canvas">
  <section class="card card--front">
    <div class="brand">
      <span class="brand__circle"></span>
      <span class="brand__name">PineHarbor</span>
    </div>
    <div class="divider"></div>
    <ul class="contact-list">
      <li class="contact-list__item">
        <span class="contact-list__icon">
          <svg width="14" height="16" viewBox="0 0 14 16"><rect x="3" y="1" width="8" height="14" rx="1.5" fill="none" stroke="#fff" stroke-width="1.6"/><circle cx="7" cy="12.3" r="0.9" fill="#fff"/></svg>
        </span>
        000 000 0000
      </li>
      <li class="contact-list__item">
        <span class="contact-list__icon">
          <svg width="16" height="16" viewBox="0 0 24 24"><path fill="#fff" d="M6.6 10.8a15.1 15.1 0 0 0 6.6 6.6l2.2-2.2c.3-.3.7-.4 1-.2 1.1.4 2.3.6 3.6.6.6 0 1 .4 1 1V20c0 .6-.4 1-1 1A17 17 0 0 1 3 4c0-.6.4-1 1-1h3.5c.6 0 1 .4 1 1 0 1.3.2 2.5.6 3.6.1.3 0 .7-.2 1z"/></svg>
        </span>
        000 000 0000
      </li>
      <li class="contact-list__item">
        <span class="contact-list__icon">
          <svg width="16" height="16" viewBox="0 0 24 24"><path fill="none" stroke="#fff" stroke-width="2" stroke-linejoin="round" d="M3 12 12 3h8v8l-9 9z"/><circle cx="16" cy="8" r="1.5" fill="#fff"/></svg>
        </span>
        info@domain.com
      </li>
      <li class="contact-list__item">
        <span class="contact-list__icon">
          <svg width="16" height="16" viewBox="0 0 24 24"><circle cx="14" cy="10" r="6" fill="none" stroke="#fff" stroke-width="2.4"/><path d="M9.5 14.5 4 20" stroke="#fff" stroke-width="3" stroke-linecap="round"/></svg>
        </span>
        www.domain.com
      </li>
    </ul>
    <p class="address">
      <svg width="12" height="16" viewBox="0 0 12 16"><path fill="var(--pin-grey)" d="M6 0a6 6 0 0 1 6 6c0 4.5-6 10-6 10S0 10.5 0 6a6 6 0 0 1 6-6zm0 3.5a2.5 2.5 0 1 0 0 5 2.5 2.5 0 0 0 0-5z"/></svg>
      NO, Adressline1,Adressline1, City
    </p>
  </section>

  <section class="card card--back">
    <div class="brand">
      <span class="brand__circle"></span>
      <span class="brand__name">PineHarbor</span>
    </div>
  </section>
</main>
</body>
</html>
```